Young adult personal development needs podcast 1400x1400 logo

We need artwork done for a podcast logo. The podcast is called The Brightmakers Show and is aimed at ages 20-30 waking up and wanting to make changes in their lives.

Using either of the two photos with the logo at bottom right of picture.

Somewhere it says: The Brightmakers Show: Educating & inspiring you to reach your greatest potential.

"The Brightmakers Show: Educating & inspiring you to reach your greatest potential.

With a strong belief in mentors and role models being a key factor to anyones success, Callum has placed himself along side the best in their fields.

Diving into movement, primal patterns, mindfulness, creativity and even the influence our gut has over our brain, these experts are going to show you how these pieces paint the picture that is your greatest potential."

```html
<!DOCTYPE html>
<html lang="en">
<head>
<meta charset="utf-8">
<title>The Brightmakers Show – Podcast Artwork</title>
<link href="https://fonts.googleapis.com/css2?family=Margarine&display=swap" rel="stylesheet">
<style>
  :root {
    --page: #ffffff;
    --sky-light: #b9d3e6;
    --sky-mid: #7f98aa;
    --sky-dark: #5b6f7d;
    --disc: #1b1a1a;
    --title-blue: #1f2ee8;
    --title-blue-bright: #1d5ff0;
    --title-grey: #9aa6b8;
    --accent-gold: #e6b81a;
    --accent-orange: #e07f10;
    --accent-yellow: #eedc1c;
    --photo-warm: #a97a66;
    --photo-deep: #6f5046;
    --mark-ink: #111111;
  }
  * { margin: 0; padding: 0; box-sizing: border-box; }
  html, body {
    width: 1200px; height: 1000px; overflow: hidden;
    background: var(--page);
  }
  .canvas { position: relative; width: 1200px; height: 1000px; }
  .cover {
    position: absolute; left: 294px; top: 194px;
    width: 614px; height: 614px; overflow: hidden;
  }
  .cover-art { position: absolute; inset: 0; }
  .host-photo {
    position: absolute; left: 0; top: 455px; width: 460px; height: 159px;
  }
  .headline {
    position: absolute; left: 0; top: 0; width: 100%;
    text-align: center;
    font-family: "Margarine", "Comic Sans MS", cursive;
    font-weight: 400;
    line-height: 1;
  }
  .headline span { display: block; position: absolute; left: 0; width: 100%; white-space: nowrap; }
  .headline-the { top: 60px; font-size: 44px; color: var(--title-blue); }
  .headline-name {
    top: 126px; font-size: 56px;
    background: linear-gradient(180deg, var(--title-blue) 0%, var(--title-blue-bright) 100%);
    -webkit-background-clip: text; background-clip: text; color: transparent;
  }
  .headline-kind {
    top: 194px; font-size: 56px;
    background: linear-gradient(180deg, var(--title-blue-bright) 0%, var(--title-grey) 55%, var(--accent-yellow) 100%);
    -webkit-background-clip: text; background-clip: text; color: transparent;
  }
  .tagline span {
    font-size: 40px;
    background: linear-gradient(90deg, var(--accent-orange) 0%, var(--accent-yellow) 50%, var(--accent-gold) 100%);
    -webkit-background-clip: text; background-clip: text; color: transparent;
  }
  .tagline-one { top: 282px; }
  .tagline-two { top: 354px; }
  .tagline-three { top: 424px; }
  .studio-mark {
    position: absolute; right: 28px; bottom: 22px;
    font-family: "Margarine", "Comic Sans MS", cursive;
    font-size: 20px; color: var(--mark-ink);
  }
</style>
</head>
<body>
<main class="canvas">
  <section class="cover">
    <svg class="cover-art" viewBox="0 0 614 614" width="614" height="614" aria-hidden="true">
      <defs>
        <radialGradient id="sky-glow" cx="50%" cy="45%" r="65%">
          <stop offset="0%" stop-color="var(--sky-light)"/>
          <stop offset="45%" stop-color="var(--sky-light)"/>
          <stop offset="62%" stop-color="var(--sky-mid)"/>
          <stop offset="100%" stop-color="var(--sky-dark)"/>
        </radialGradient>
      </defs>
      <rect width="614" height="614" fill="url(#sky-glow)"/>
      <circle cx="309" cy="277" r="251" fill="var(--disc)"/>
    </svg>

    <svg class="host-photo" viewBox="0 0 460 159" preserveAspectRatio="none" role="img" aria-label="Photo of the host seen from behind with arms stretched wide toward the disc">
      <defs>
        <radialGradient id="photo-tone" cx="50%" cy="80%" r="60%">
          <stop offset="0%" stop-color="var(--photo-warm)" stop-opacity="0.95"/>
          <stop offset="55%" stop-color="var(--photo-deep)" stop-opacity="0.55"/>
          <stop offset="100%" stop-color="var(--photo-deep)" stop-opacity="0"/>
        </radialGradient>
      </defs>
      <rect width="460" height="159" fill="url(#photo-tone)"/>
    </svg>

    <h1 class="headline">
      <span class="headline-the">The</span>
      <span class="headline-name">Brightmakers</span>
      <span class="headline-kind">Show:</span>
    </h1>
    <p class="headline tagline">
      <span class="tagline-one">Educating &amp; inspiring you</span>
      <span class="tagline-two">to reach your greatest</span>
      <span class="tagline-three">potential.</span>
    </p>

    <div class="studio-mark">Northvale Growth</div>
  </section>
</main>
</body>
</html>
```